Cover design needed for scholarship book whose intended audience is students with medical conditions

I need a book cover designed for a book called, “The Thistle Grant: Ways To Change Your Health Challenge Into Open Funds For University.” This book is aimed at students with a variety of medical conditions. I wrote The Thistle Grant after I received a medical-based scholarship ($96,000) to attend college and law school based on my allergies to pollen—hence the title. However, this government program applies to just about any medical condition—not just allergies. I have assisted students in applying for this program who suffer from many different medical conditions. So I would like the cover design to convey that message—that this program applies to many different medical conditions. One of the big misconceptions about medical-based scholarships is you will only qualify if you have a really serious medical condition. So I would like to see some cover designs that list some common medical conditions in order to convey to the reader that many different medical conditions qualify. A few possible medical conditions are allergies, asthma, ADHD, depression, anxiety, back pain, eating disorders, bipolar, sleep disorders, and OCD. Possible ways to convey this may be to have the names of some of these common medical conditions written on graduation caps or randomly dispersed in the background, etc. However, this isn’t the only theme I would like to see. In essence, I give you creative liberty to wow me with your design prowess. The point of crowd design is to get variety of designs to choose from that I may not have thought of on my own. I have dabbled with some ideas that blend the themes of the education world and the medical world and I think this is the essence of the book. What ever you come up with, it needs to make it clear at a glance that this book helps you pay for college on the basis of your medical condition—whatever medical condition that may be. To see a simple mock up I did (that I don't want to use) go to healthawardfinder.example

The book is 153 pages on 5x8 paper. I am planning to print the book through PageForge, so the cover should adhere to the PageForge design requirements. I can provide the PageForge template if needed.

Updates: Please be able to provide a few updates to the cover design if your design is selected. After choosing the final design, physical proofs of the book will be ordered so I can see what your design looks like in real life. After the proofs are reviewed, I may need some minor changes (i.e., maybe the back cover text needs a new font size, etc..) Also, after I use the proofs to solicit endorsements, I am planning to purchase my own ISBN number and barcode. I would like the designer to be able to update my cover to include a new ISBN and barcode after the initial proofs are printed which should be 3-4 weeks later. So please be able to provide a few updates to the cover design if your design is selected.

Target Market(s)

Students/parents who are planning to attend college and have some type of medical condition

Industry/Entity Type

College

Font styles to use
Serif

Requirements
Must have
• My project must have a general education/medical theme
Nice to have
• I'd like to see some designs that include random medical conditions dispersed on the cover. Maybe a different medical condition written on several different graduation caps, or some other context.
Should not have
• The cover design should not depict persons with severe medical conditions--i.e., people in wheelchairs, hospital beds, etc.

```html
<!DOCTYPE html>
<html lang="en">
<head>
<meta charset="utf-8">
<title>The Thistle Grant – Cover Wrap</title>
<link rel="stylesheet" href="https://fonts.googleapis.com/css2?family=Jost:wght@300;400&family=Oswald:wght@400;500;600&family=Fjalla+One&family=Arimo:wght@400&display=swap">
<style>
  :root{
    --bg:#2a3133;
    --navy:#0b1650;
    --ink:#12307a;
    --blue:#1e5bc6;
    --blue-deep:#0d3fae;
    --sky:#cfe3f7;
    --sky-light:#eef5fc;
    --band-light:#9cc8f0;
    --white:#ffffff;
  }
  *{box-sizing:border-box;margin:0;padding:0}
  html,body{width:1200px;height:1200px;overflow:hidden;background:var(--bg)}
  .wrap{position:absolute;left:25px;top:160px;width:1150px;height:880px;display:flex;box-shadow:0 20px 50px rgba(0,0,0,.45)}

  /* back cover */
  .back{position:relative;width:550px;height:880px;overflow:hidden;
    background:radial-gradient(ellipse 70% 45% at 55% 38%,#f4f9ff 0%,#bcd9f6 40%,transparent 75%),
               linear-gradient(180deg,#3d8ae0 0%,#5aa0ea 35%,#3f85dd 60%,#1d5ec8 100%);}
  .back-heading{position:absolute;left:40px;top:125px;width:470px;font-family:"Fjalla One",sans-serif;
    color:var(--navy);font-size:25px;line-height:1.25;text-align:center}
  .back-copy{position:absolute;left:40px;top:215px;width:470px;font-family:"Arimo",sans-serif;
    color:var(--navy);font-size:14.2px;line-height:1.32;text-align:justify}
  .back-copy p+p{margin-top:16px}
  .author{position:absolute;left:40px;top:585px;width:470px;display:flex;gap:16px}
  .author-photo{flex:0 0 90px;height:150px;background:linear-gradient(160deg,#6d7d4a,#b6a98a 55%,#e8edf2)}
  .author-bio{font-family:"Arimo",sans-serif;color:var(--navy);font-size:13.6px;line-height:1.28;text-align:justify}

  /* spine */
  .spine{position:relative;width:50px;height:880px;background:linear-gradient(90deg,#1e56c2,#2a6ad6 50%,#1a50ba)}
  .spine-text{position:absolute;left:50%;top:40px;transform:translateX(-50%);writing-mode:vertical-rl;
    display:flex;align-items:center;gap:10px;color:var(--white);white-space:nowrap}
  .spine-title{font-family:"Oswald",sans-serif;font-weight:600;font-size:24px;letter-spacing:2px}
  .spine-divider{width:1px;height:22px;background:var(--white)}
  .spine-sub{font-family:"Arimo",sans-serif;font-size:11px;line-height:1.2;writing-mode:vertical-rl;white-space:normal;height:300px}

  /* front cover */
  .front{position:relative;width:550px;height:880px;overflow:hidden;
    background:linear-gradient(180deg,var(--sky) 0%,var(--sky-light) 22%,#f7fbff 40%)}
  .front-title{position:absolute;left:0;top:60px;width:100%;text-align:center}
  .title-top{font-family:"Jost",sans-serif;font-weight:300;color:var(--blue-deep);font-size:62px;letter-spacing:2px;line-height:1}
  .title-main{position:relative;display:inline-block;margin-top:6px;padding:0 30px;
    font-family:"Oswald",sans-serif;font-weight:600;color:var(--navy);font-size:74px;line-height:1.1;letter-spacing:1px;
    background:linear-gradient(90deg,transparent,var(--band-light) 12%,var(--band-light) 88%,transparent)}
  .hero{position:absolute;left:0;top:215px;width:550px;height:555px;
    background:linear-gradient(180deg,#f1f7fd 0%,#dbeaf8 35%,#9fb4d0 62%,#2a3568 82%,#101a46 100%)}
  .condition{position:absolute;font-family:"Oswald",sans-serif;font-weight:500;color:var(--blue-deep);
    font-size:17px;letter-spacing:.3px;white-space:nowrap}
  .condition.lg{font-size:22px}
  .subtitle-band{position:absolute;left:0;top:770px;width:100%;height:74px;background:var(--blue);
    color:var(--white);font-family:"Jost",sans-serif;font-size:20px;letter-spacing:1px;text-align:center;
    text-transform:uppercase;line-height:1.3;padding-top:10px}
  .base-strip{position:absolute;left:0;top:844px;width:100%;height:36px;background:var(--navy)}
</style>
</head>
<body>
<div class="wrap">

  <section class="back">
    <h2 class="back-heading">How Anyone Can Get Free Money for College<br>on the Basis of Their Medical Condition!</h2>
    <div class="back-copy">
      <p>The first book ever to expose the secret world of medical-based scholarships, The Thistle Grant shows you how to turn any medical condition into free money for college! Whether your medical condition is incredibly serious or just mildly annoying, this book can save you a fortune in college expenses! Medical-based scholarships provide students with an exciting opportunity to pay for college on the basis of just about any medical condition—allergies, ADHD, anxiety, depression, back pain—the list goes on and on. But to take advantage of this program, first you need to know how to apply!</p>
      <p>The Thistle Grant is a step-by-step guide that walks students and parents through the simple application process for the medical-based scholarship program. It doesn't matter where you live, what college you plan to attend, or what medical condition you suffer from—The Thistle Grant applies to you! With the ever-increasing cost of a college education, if you suffer from any medical condition whatsoever, The Thistle Grant is a must read!</p>
    </div>
    <div class="author">
      <div class="author-photo" role="img" aria-label="Author portrait photo"></div>
      <p class="author-bio">Marcus Hale is an attorney–author who paid for his own degrees through the medical-based scholarship program on the basis of everyday health challenges he has lived with since childhood. Marcus has served as a state public counsel and now works as a policy advisor for a federal education office. He has helped many students and families apply for this program with success.</p>
    </div>
  </section>

  <section class="spine">
    <div class="spine-text">
      <span class="spine-title">THE THISTLE GRANT</span>
      <span class="spine-divider"></span>
      <span class="spine-sub">Ways To Change Your Health Challenge Into Open Funds For University</span>
    </div>
  </section>

  <section class="front">
    <div class="hero" role="img" aria-label="Photo of cheering graduates in gowns throwing mortarboard caps into a bright sky"></div>
    <header class="front-title">
      <div class="title-top">THE THISTLE</div>
      <div class="title-main">GRANT</div>
    </header>
    <span class="condition" style="left:55px;top:268px">BACK PAIN</span>
    <span class="condition" style="left:220px;top:268px">EATING DISORDERS</span>
    <span class="condition" style="left:440px;top:295px;transform:rotate(22deg)">DIABETES</span>
    <span class="condition lg" style="left:320px;top:325px;transform:rotate(6deg)">ASTHMA</span>
    <span class="condition" style="left:60px;top:358px;transform:rotate(4deg)">SLEEP DISORDERS</span>
    <span class="condition lg" style="left:95px;top:460px;transform:rotate(-4deg)">ADHD</span>
    <span class="condition lg" style="left:240px;top:468px;transform:rotate(4deg)">ANXIETY</span>
    <span class="condition lg" style="left:350px;top:450px;transform:rotate(10deg)">DEPRESSION</span>
    <span class="condition lg" style="left:350px;top:510px;transform:rotate(40deg)">OCD</span>
    <span class="condition lg" style="left:435px;top:528px">ALLERGIES</span>
    <div class="subtitle-band">Ways To Change Your Health Challenge<br>Into Open Funds For University</div>
    <div class="base-strip"></div>
  </section>

</div>
</body>
</html>
```